Email Marketing for Post-wren

I am a sports photographer and I would like to have an email distribution that I can send out after an event or have something go out on a more regular basis.

juniperridge-peakshot.com

I can supply the looks and so on I am looking for a template that I can reuse time and time again.

I want something that works with Postwren.

http://postwrenmail.com

It must conform to there templates and I would like to be able to put some photo's in the template as well.

Target Market(s)

Parents and Families attending events and wishing to purchase photos from that day.

Industry/Entity Type

Marketing

Font styles to use
Serif

Requirements
Must have
• Must have my logo.
• Must use the same font museo 500.
• Must be Red, Grey and White same as the logo.
• Must have Facebook links https://www.pallorium.net/JuniperRidgePeakshot
• Must have twitter links @junipeakshot
• Must have email address info@juniperridge-peakshot.com
• Must have room for other company logo's in the future
• Should be broken down in sections

```html
<!DOCTYPE html>
<html lang="en">
<head>
<meta charset="utf-8">
<title>Juniper Ridge Peakshot – Event Newsletter</title>
<link rel="stylesheet" href="https://fonts.googleapis.com/css2?family=Arimo:wght@400;700&display=swap">
<style>
  :root {
    --red: #d2232a;
    --white: #ffffff;
    --grey: #5a5a5a;
    --grey-dark: #333333;
    --sky-top: #2c8fb0;
    --sky-mid: #5fb9cf;
    --pool-deep: #1f6f84;
    --pool-light: #8fd3dc;
    --footer-bg: #f2f2f2;
  }
  * { box-sizing: border-box; margin: 0; padding: 0; }
  html, body { width: 769px; height: 1200px; overflow: hidden; }
  body { font-family: "Arimo", Arial, sans-serif; background: var(--white); }
  .newsletter { position: relative; width: 769px; height: 1200px; overflow: hidden; }

  .hero-backdrop {
    position: absolute; left: 0; top: 0; width: 769px; height: 1057px;
    background: linear-gradient(180deg, var(--sky-top) 0%, var(--sky-mid) 40%, var(--pool-deep) 55%, var(--pool-light) 75%, #b9e4e8 100%);
  }

  .masthead { position: absolute; left: 68px; top: 42px; }
  .brand-title {
    color: var(--white); font-weight: 400; font-size: 34px; line-height: 38px;
    letter-spacing: 0.5px; text-transform: uppercase;
  }
  .brand-title strong { font-weight: 700; }
  .event-date {
    margin-top: 2px; text-align: right;
    color: var(--white); font-size: 18px; line-height: 22px;
  }
  .event-date sup { font-size: 10px; }

  .social-top { position: absolute; right: 12px; top: 14px; display: flex; gap: 14px; }
  .social-top span { display: block; width: 30px; height: 30px; background: var(--white); border-radius: 4px; }

  .gallery { position: absolute; left: 69px; top: 197px; display: flex; gap: 15px; }
  .gallery-photo { width: 201px; height: 174px; }
  .gallery-photo.city { background: linear-gradient(180deg, #6fa6d8, #2f4f73); }
  .gallery-photo.harbour { background: linear-gradient(180deg, #1d3f7a, #d98a4e 60%, #3d6c8f); }
  .gallery-photo.palm { background: linear-gradient(180deg, #7cc3e6, #3f7a3c 70%, #6c9a55); }

  .intro-copy {
    position: absolute; left: 69px; top: 382px; width: 640px;
    color: var(--white); font-size: 16.5px; line-height: 23px;
  }

  .brand-watermark {
    position: absolute; left: 0; width: 769px; top: 640px; text-align: center;
    color: rgba(255,255,255,0.75); font-size: 58px; letter-spacing: 1px;
  }

  .headline {
    position: absolute; left: 46px; top: 820px; width: 430px;
    color: var(--red); font-size: 40px; line-height: 51px; font-weight: 400;
    text-transform: uppercase;
  }
  .headline strong { font-weight: 700; }

  .footer {
    position: absolute; left: 0; top: 1057px; width: 769px; height: 143px;
    background: var(--footer-bg); border-top: 3px solid var(--red);
  }
  .contact { position: absolute; left: 26px; top: 14px; color: var(--grey-dark); font-size: 14px; line-height: 17px; }
  .contact h2 { font-size: 15px; font-weight: 700; }
  .contact .follow { margin-top: 2px; font-size: 12px; }
  .social-foot { display: flex; gap: 6px; margin-top: 4px; }
  .social-foot span { display: block; width: 14px; height: 14px; background: var(--grey); border-radius: 2px; }

  .logo {
    position: absolute; right: 26px; top: 52px;
    display: flex; align-items: center; gap: 8px;
    color: var(--red); font-size: 15px; font-weight: 700; text-transform: uppercase;
  }
  .logo i { display: block; width: 14px; height: 14px; background: var(--red); border-radius: 50%; }
</style>
</head>
<body>
<div class="newsletter">
  <div class="hero-backdrop" role="img" aria-label="Photo of a resort swimming pool with umbrellas under a blue sky"></div>

  <header class="masthead">
    <h1 class="brand-title">Juniper Ridge<br><strong>Peakshot</strong></h1>
    <p class="event-date">July 25<sup>th</sup></p>
  </header>

  <div class="social-top" aria-label="Social links"><span></span><span></span><span></span></div>

  <div class="gallery">
    <div class="gallery-photo city" role="img" aria-label="Event photo: city towers"></div>
    <div class="gallery-photo harbour" role="img" aria-label="Event photo: harbour at dusk"></div>
    <div class="gallery-photo palm" role="img" aria-label="Event photo: palm tree against sky"></div>
  </div>

  <p class="intro-copy">Integer in dictum lectus. Duis eu mauris lorem. Nam sit amet nisi et eslort auctor ornare id lobortis nisl. Morbi fringilla est risus. vit sodales enimultri ces gravida. Ut efficitur condimentum justo elum interdum.</p>

  <p class="brand-watermark">Juniper Ridge Peakshot</p>

  <h2 class="headline"><strong>Morbi fringilla est risus,</strong> vitae senim ultrices gravida.</h2>

  <footer class="footer">
    <div class="contact">
      <h2>Contact Us:</h2>
      <p>info@juniperridge-peakshot.com</p>
      <p>Larchmont NSW 2071 - Australia</p>
      <p>Mobile: +61 400 555 017</p>
      <p class="follow">Follow On</p>
      <div class="social-foot"><span></span><span></span><span></span></div>
    </div>
    <div class="logo"><i></i>Juniper Ridge Peakshot</div>
  </footer>
</div>
</body>
</html>
```